Tovex - Business Card Design

Design a modern masculine business card for our business

Target Market(s)

Private Market

Industry/Entity Type

Construction

Contact Information for Business Card

Company Name - Name of Person - Address - email address - contact number

Font styles to use
Serif
Sans Serif

Colors
0094D4
00A9DD
6FCCEA
C7EBF8
E9F6FB
00AB8E
00BBA5
67D7C9
C6EFE9
E9F9F6
F0912C
F2A743
F7CA91
FBE8D2
FDF5EE

Requirements
Must have
• Use company logo provided
Nice to have
• Company Logo

```html
<!DOCTYPE html>
<html lang="en">
<head>
<meta charset="utf-8">
<title>Tovex Construction – Business Card</title>
<link href="https://fonts.googleapis.com/css2?family=Montserrat:wght@400;500;800&display=swap" rel="stylesheet">
<style>
  :root {
    --orange: #f2752e;
    --ink: #121212;
    --paper: #ffffff;
    --stage: #3a3a3a;
  }
  * { margin: 0; padding: 0; box-sizing: border-box; }
  html, body { width: 1200px; height: 900px; overflow: hidden; }
  body {
    background: var(--stage);
    font-family: "Montserrat", Arial, sans-serif;
    position: relative;
  }
  .card {
    position: absolute;
    width: 560px;
    height: 320px;
    overflow: hidden;
    box-shadow: 0 14px 30px rgba(0,0,0,.45);
  }
  /* Front */
  .card-front { left: 70px; top: 90px; background: var(--orange); }
  .card-front .wordmark {
    position: absolute; left: 0; right: 0; top: 120px;
    text-align: center; color: var(--paper);
    font-weight: 800; font-size: 72px; letter-spacing: 6px; line-height: 1;
  }
  .wordmark .mark-square {
    display: inline-block; width: 0.32em; height: 0.32em;
    background: currentColor; margin-right: 16px; vertical-align: middle;
  }
  /* Back */
  .card-back { left: 570px; top: 490px; background: var(--paper); }
  .card-back .wordmark {
    position: absolute; right: 40px; top: 40px;
    color: var(--ink); font-weight: 800; font-size: 44px; letter-spacing: 4px; line-height: 1;
  }
  .card-back .wordmark .mark-square { background: var(--orange); margin-right: 10px; }
  .name-bar {
    position: absolute; left: 0; top: 128px; width: 22px; height: 54px;
    background: var(--orange);
  }
  .person { position: absolute; left: 40px; top: 130px; }
  .person-name { font-weight: 800; font-size: 24px; letter-spacing: .5px; }
  .person-name .first { color: var(--orange); }
  .person-name .last { color: var(--ink); }
  .person-role { font-weight: 500; font-size: 15px; color: var(--ink); margin-top: 4px; }
  .contact-list {
    position: absolute; left: 40px; bottom: 50px; list-style: none;
    font-size: 13px; color: var(--ink); font-weight: 500;
  }
  .contact-list li { display: flex; align-items: center; gap: 8px; height: 20px; }
  .contact-list svg { width: 13px; height: 13px; fill: var(--orange); }
  .address {
    position: absolute; right: 36px; top: 150px;
    font-size: 13px; font-weight: 500; color: var(--ink); text-align: right; line-height: 1.5;
  }
  .swoosh { position: absolute; left: 0; bottom: 0; width: 560px; height: 140px; }
</style>
</head>
<body>
  <section class="card card-front">
    <div class="wordmark"><span class="mark-square"></span>TOVEX</div>
  </section>

  <section class="card card-back">
    <div class="wordmark"><span class="mark-square"></span>TOVEX</div>

    <div class="name-bar"></div>
    <div class="person">
      <p class="person-name"><span class="first">MARTIN</span> <span class="last">KELLER</span></p>
      <p class="person-role">Managing Director</p>
    </div>

    <address class="address">42-11 Harbor Ave 9<br>Ridgeview, NY 11390</address>

    <ul class="contact-list">
      <li><svg viewBox="0 0 24 24"><path d="M6.6 10.8a15.1 15.1 0 0 0 6.6 6.6l2.2-2.2c.3-.3.7-.4 1-.2 1.1.4 2.3.6 3.6.6.6 0 1 .4 1 1V20c0 .6-.4 1-1 1A17 17 0 0 1 3 4c0-.6.4-1 1-1h3.5c.6 0 1 .4 1 1 0 1.3.2 2.5.6 3.6.1.3 0 .7-.2 1z"/></svg>555.210.4387</li>
      <li><svg viewBox="0 0 24 24"><path d="M2 5h20v14H2z M3 6l9 7 9-7" stroke="#fff" stroke-width="1.5"/></svg>info@tovex-build.com</li>
      <li><svg viewBox="0 0 24 24"><circle cx="12" cy="12" r="10"/><path d="M2 12h20M12 2c3 3 3 17 0 20M12 2c-3 3-3 17 0 20" stroke="#fff" stroke-width="1.3" fill="none"/></svg>www.tovex-build.com</li>
    </ul>

    <svg class="swoosh" viewBox="0 0 560 140" preserveAspectRatio="none">
      <path d="M0 124 C 180 118, 320 100, 420 50 C 470 26, 520 14, 560 10 L560 140 L0 140 Z" fill="var(--orange)"/>
      <path d="M0 118 C 180 112, 320 94, 420 44 C 470 20, 520 8, 560 4" stroke="var(--ink)" stroke-width="3" fill="none"/>
    </svg>
  </section>
</body>
</html>
```